Zanquerra Business Card Design

Zanquerra is a small and new restaurant/ bar location in Hong Kong. The name "Djibouti" derives from an African country. There is no specific reason behind other than the fact, that the bar is somewhat inspired by African elements (only inspired but not purely based on African cuisine etc.).

The bar is somewhat a fusion of African, Mediterranean and Oriental (Old French Vietnam) elements.

However, it is very imperative to stress, that the overall look and feel of Zanquerra is a very high end cocktail lounge/ bar location. The bar is tucked away in a hidden alley, so people will have to know about it. The idea is to send the consumer off in an Escape or hidden remote location where they are at ease in a hip, stylish and trendy environment.

The card needs to feel high-end.

Final logo artwork has been attached and also pictures of the bar/ restaurant itself. The logo ie monkey head cannot be modified. However, the background color and the color of the type "ZANQUERRA" can be changed.

The following details need to fit onto the business card. Of course they can be arranged to your liking:

LOGO

Tobin Le
Partner

+852 90817364
xxx@zanquerra-bar.com
www.zanquerra-bar.com
4C, Pelham Lane, Wan Chai, Hong Kong

Industry/Entity Type

Restaurant

```html
<!DOCTYPE html>
<html lang="en">
<head>
<meta charset="utf-8">
<title>Zanquerra Business Card Options</title>
<link rel="stylesheet" href="https://fonts.googleapis.com/css2?family=Cinzel:wght@400;700&family=Open+Sans:wght@400;600;700&family=Josefin+Sans:wght@400&display=swap">
<style>
  :root{
    --board:#8a5e3b;
    --label:#ffffff;
    --blue-light:#12a9e3;
    --blue-mid:#1b76c0;
    --blue-deep:#0d3f86;
    --brown-dark:#2a1a12;
    --silver-light:#f7f7f7;
    --silver-mid:#dcdcdc;
    --ink-blue:#1b6fb5;
    --ring-grey:#8c96a3;
    --disc-grey:#55585c;
  }
  *{margin:0;padding:0;box-sizing:border-box}
  html,body{width:1200px;height:836px;overflow:hidden;background:var(--board)}
  .board{position:relative;width:1200px;height:836px;background:var(--board)}
  .option-label{
    position:absolute;color:var(--label);
    font-family:"Cinzel",serif;font-size:23px;letter-spacing:1px;
    transform:translateX(-50%);white-space:nowrap;
  }
  .card{position:absolute;overflow:hidden;box-shadow:4px 5px 6px rgba(0,0,0,.45)}
  .card svg{position:absolute;left:0;top:0}
  .brand-name{font-family:"Cinzel",serif;font-weight:700;position:absolute;white-space:nowrap;transform:translateX(-50%)}
  .brushed{
    background:
      repeating-linear-gradient(90deg,rgba(0,0,0,.035) 0 1px,transparent 1px 4px,rgba(255,255,255,.6) 4px 5px,transparent 5px 9px),
      linear-gradient(100deg,var(--silver-mid),var(--silver-light) 45%,#ffffff 60%,var(--silver-mid));
  }

  /* front option 1 */
  .card-front{left:80px;top:92px;width:464px;height:265px;
    background:linear-gradient(160deg,var(--blue-light),var(--blue-mid) 45%,var(--blue-deep))}
  .front-contact{position:absolute;right:28px;text-align:right;font-family:"Open Sans",sans-serif;
    font-size:11.5px;color:var(--ink-blue);line-height:1;white-space:nowrap}
  .front-contact b{font-weight:700}
  .front-web{font-weight:700;font-size:12px}
  .front-person{position:absolute;right:30px;top:212px;text-align:right;color:#fff;font-family:"Josefin Sans",sans-serif;line-height:1}
  .front-person .person-name{font-size:19px;letter-spacing:1px}
  .front-person .person-role{font-size:11px;letter-spacing:1.5px;margin-top:4px}

  /* back option 1 */
  .card-back-blue{left:618px;top:93px;width:466px;height:265px;
    background:linear-gradient(180deg,var(--blue-light),var(--blue-mid) 50%,var(--blue-deep))}
  .back-web{position:absolute;left:292px;top:167px;transform:translateX(-50%);color:#fff;
    font-family:"Open Sans",sans-serif;font-weight:700;font-size:10.5px;white-space:nowrap}

  /* back option 4 */
  .card-back-silver{left:364px;top:445px;width:466px;height:269px}
</style>
</head>
<body>
<main class="board">
  <p class="option-label" style="left:321px;top:52px">Front OPTION 1</p>
  <p class="option-label" style="left:888px;top:54px">BACK OPTION 1</p>
  <p class="option-label" style="left:619px;top:742px">BACK OPTION 4</p>

  <section class="card card-front">
    <svg width="464" height="265" viewBox="0 0 464 265">
      <defs>
        <pattern id="brush" width="9" height="10" patternUnits="userSpaceOnUse">
          <rect width="9" height="10" fill="#f3f3f3"/>
          <rect x="1" width="1" height="10" fill="#dedede"/>
          <rect x="5" width="1" height="10" fill="#ffffff"/>
        </pattern>
      </defs>
      <path d="M0,66 C140,36 300,8 464,28 L464,172 C400,176 330,196 270,228 C190,252 90,226 0,196 Z" fill="url(#brush)"/>
      <path d="M0,66 C140,36 300,8 464,28" fill="none" stroke="var(--brown-dark)" stroke-width="5"/>
      <path d="M0,73 C140,43 300,15 464,35" fill="none" stroke="#a8adb3" stroke-width="3"/>
      <path d="M0,196 C90,226 190,252 270,228 C330,196 400,176 464,172" fill="none" stroke="var(--brown-dark)" stroke-width="5"/>
      <path d="M0,203 C90,233 190,259 270,235 C330,203 400,183 464,179" fill="none" stroke="#a8adb3" stroke-width="3"/>
      <circle cx="139" cy="133" r="42" fill="#ffffff" stroke="var(--brown-dark)" stroke-width="3"/>
    </svg>
    <p class="brand-name" style="left:139px;top:186px;font-size:24px;color:var(--brown-dark)">ZANQUERRA</p>
    <p class="front-contact" style="top:73px"><b>T:</b> +852 90817364</p>
    <p class="front-contact" style="top:89px"><b>E:</b> xxx@zanquerra-bar.com</p>
    <p class="front-contact front-web" style="top:109px">www.zanquerra-bar.com</p>
    <p class="front-contact" style="top:135px">4C, Pelham Lane</p>
    <p class="front-contact" style="top:150px">Wan Chai, Hong Kong</p>
    <div class="front-person">
      <p class="person-name">TOBIN LE</p>
      <p class="person-role">PARTNER</p>
    </div>
  </section>

  <section class="card card-back-blue">
    <svg width="466" height="265" viewBox="0 0 466 265">
      <circle cx="12" cy="132" r="122" fill="var(--ring-grey)" stroke="#1d3f6e" stroke-width="3"/>
      <circle cx="12" cy="132" r="112" fill="var(--disc-grey)"/>
    </svg>
    <p class="brand-name" style="left:292px;top:100px;font-size:38px;color:#ffffff">ZANQUERRA</p>
    <p class="back-web">www.zanquerra-bar.com</p>
  </section>

  <section class="card card-back-silver brushed">
    <svg width="466" height="269" viewBox="0 0 466 269">
      <circle cx="225" cy="100" r="62" fill="#ffffff" stroke="var(--brown-dark)" stroke-width="3"/>
    </svg>
    <p class="brand-name" style="left:225px;top:180px;font-size:34px;color:var(--brown-dark)">ZANQUERRA</p>
  </section>
</main>
</body>
</html>
```